Pack - Adventurous, Fun, Exciting, Social Fitness Club needs a Webpage with attitude!

Pack... we're a fun, social, outdoor fitness club that needs not just a homepage designed for our website, but in the process a "personality" for our unique, innovative and cheeky brand.
We pride ourselves on getting our members outdoors trying new, exciting physical activities in an effort to find joy in an active lifestyle, and sharing that experience with other like minded people. We offer:
- Personal Training (1-on-1 Fitness Training)
- Group Fitness Classes (Boxing, Pilates, etc)
- Boot Camps (Military Style - Sandbags, Ropes, Tyres, etc)
- Events (Fun Runs, Triathlons, Ocean Swims, Treks, etc)
- Adventures(Quorra Ridge Trek, Rock Climbing, Kayaking, etc)
Our tag line is 'No Judgements. No Limits!' The homepage should be exciting, adventurous and innovative, illustrating the values of our brand: possibility, thirst for life, personal accomplishment & freedom. It should be fun, friendly & inviting.
A few of our key benefits to members are:
- No Boring Workouts
- No Joining Fees or Long Term Contracts
- Results Guaranteed
The links below should give you a rough idea of the sort of "feel" we're after (vibrant, active, adventurous ).
http://www.campusroamer.com.au/
http://www.layoutgoblin.com/website-templates/31924.html
http://www.layoutgoblin.com/website-templates/32751.html
http://www.velmora.com/
Target Market(s)
Real, Everyday People - Men & Women (30:70) aged mainly between 21-40, who want a more exciting and enjoyable fitness experience than your typical gym offers.
Industry/Entity Type
Fitness
Requirements
Must have
- Strong, uplifting and motivating images of people enjoying fitness/physical activities outdoors

```html
<!DOCTYPE html>
<html lang="en">
<head>
<meta charset="utf-8">
<title>Pack – Outdoor Fitness Club</title>
<link href="https://fonts.googleapis.com/css2?family=Arimo:ital,wght@0,400;0,700;1,400&family=Arvo:wght@400;700&family=Oswald:wght@500&family=Roboto+Condensed:wght@700&display=swap" rel="stylesheet">
<style>
:root{
  --black:#0d0d0d;
  --forest-dark:#3f7d12;
  --forest:#7cbc22;
  --forest-light:#d8ec7a;
  --frame:#4e6b26;
  --orange:#f05a0c;
  --orange-light:#ff8a1c;
  --yellow:#ffd400;
  --white:#ffffff;
  --ink:#1c1c1c;
  --sky:#a9cdea;
  --wood:#6a3616;
}
*{margin:0;padding:0;box-sizing:border-box}
html,body{width:1200px;height:1011px;overflow:hidden}
body{position:relative;font-family:"Arimo",Arial,sans-serif;color:var(--ink);background:var(--forest)}
.forest-backdrop{position:absolute;inset:0;background:
  radial-gradient(ellipse at 50% 30%,var(--forest-light) 0%,#b3d94a 35%,var(--forest) 65%,var(--forest-dark) 100%)}
.top-bar{position:absolute;left:0;top:0;width:1200px;height:37px;background:linear-gradient(#5a5a5a,#1a1a1a 60%,var(--black));font-family:"Roboto Condensed",sans-serif;font-size:12.5px;color:var(--white)}
.top-bar .account{position:absolute;left:172px;top:10px}
.top-bar .account .signup{color:var(--yellow)}
.top-bar .utility{position:absolute;right:140px;top:10px}
.top-bar .social{position:absolute;right:52px;top:8px;display:flex;gap:6px}
.top-bar .social span{display:block;width:36px;height:20px;border-radius:3px;background:#3f5f9c;font:400 9px/20px "Arimo",sans-serif;text-align:center;color:var(--white)}
.top-bar .social span+span{background:#3fa6d8}
.brand{position:absolute;left:168px;top:68px;display:flex;align-items:center;gap:10px;font:700 62px/1 "Arimo",sans-serif;color:var(--orange)}
.brand i{display:block;width:22px;height:22px;border-radius:50%;background:var(--black)}
.call-us{position:absolute;right:148px;top:66px;text-align:right;color:var(--black);font-family:"Arimo",sans-serif}
.call-us small{display:block;font-size:17px;font-weight:700;letter-spacing:.3px}
.call-us strong{display:block;font-size:33px;line-height:1;letter-spacing:-.5px}
.main-nav{position:absolute;right:143px;top:132px;display:flex;gap:36px;font:700 15px "Roboto Condensed",sans-serif;color:var(--white);letter-spacing:-.2px;text-shadow:-1px -1px 0 var(--black),1px -1px 0 var(--black),-1px 1px 0 var(--black),1px 1px 0 var(--black),2px 2px 0 var(--black)}
.panel{position:absolute;border:4px solid rgba(78,107,38,.85);border-radius:8px;overflow:hidden;box-shadow:0 0 0 1px rgba(255,255,255,.25)}
.photo{position:absolute}
.hero{left:162px;top:169px;width:597px;height:322px}
.hero .photo{inset:0;background:linear-gradient(180deg,#6fa8dc 0%,#bcd8ef 55%,#d9cdb3 75%,#8a7a60 100%)}
.hero .photo::after{content:"";position:absolute;right:0;top:0;width:300px;height:250px;background:linear-gradient(120deg,#a89a80,#7b6d58);border-radius:60px 0 0 0}
.hero h1{position:absolute;left:22px;top:18px;font:400 50px/54px "Arvo",serif;color:var(--black);letter-spacing:-1px}
.hero ul{position:absolute;left:24px;top:136px;list-style:none;font-size:15px;line-height:22px;color:var(--black)}
.btn{display:inline-block;background:linear-gradient(var(--orange-light),var(--orange) 55%,#d84506);color:var(--white);font-weight:700;border-radius:4px;text-align:center;box-shadow:0 1px 2px rgba(0,0,0,.4)}
.hero .btn{position:absolute;left:20px;top:209px;width:190px;height:30px;line-height:30px;font-size:15.5px}
.testimonial{position:absolute;left:0;right:0;bottom:0;height:68px;background:rgba(40,32,22,.78);color:var(--white);padding:6px 18px}
.testimonial h2{font:400 19px "Arimo",sans-serif;margin-bottom:4px}
.testimonial p{font-size:11.5px;line-height:15px}
.signup-panel{left:773px;top:169px;width:290px;height:322px}
.signup-panel .photo{inset:0;background:linear-gradient(135deg,#8a4a1e,var(--wood) 60%,#4a240d)}
.signup-panel h2{position:absolute;left:16px;top:12px;font:700 33px/33px "Arimo",sans-serif;color:var(--white);text-shadow:1px 1px 2px rgba(0,0,0,.5)}
.signup-panel h2 em{font-style:normal;color:var(--yellow)}
.signup-panel h2 span{font-size:26px}
.member-card{position:absolute;left:30px;top:90px;width:155px;height:75px;background:#f6f2e4;border-radius:4px;transform:rotate(-6deg);box-shadow:2px 3px 6px rgba(0,0,0,.5)}
.perks{position:absolute;left:16px;top:170px;list-style:none;font-size:11.5px;line-height:14px;font-style:italic;color:var(--white)}
.perks li::before{content:"";display:inline-block;width:6px;height:6px;border-radius:50%;background:var(--white);margin-right:9px;vertical-align:1px}
.field{position:absolute;top:248px;width:126px;height:26px;background:var(--white);border:1px solid #bbb;font-size:12px;color:#888;padding:6px 9px}
.field.name{left:13px}.field.email{left:151px}
.newsletter{position:absolute;left:14px;top:292px;font-size:12px;font-style:italic;color:var(--white);display:flex;align-items:center;gap:7px}
.newsletter b{display:block;width:14px;height:14px;background:var(--white);border-radius:2px;color:#1e5aa8;font:700 12px/14px "Arimo",sans-serif;text-align:center}
.signup-panel .btn{position:absolute;right:12px;top:285px;width:90px;height:26px;line-height:26px;font-size:13.5px}
.offer{top:508px;width:290px;height:229px}
.offer .photo{inset:0}
.offer.training{left:164px}
.offer.training .photo{background:linear-gradient(160deg,#e8e35c,#c6d830 45%,#8fbf2a)}
.offer.group{left:466px}
.offer.group .photo{background:linear-gradient(160deg,#9fc85a,#e6ead0 55%,#d2dd8c)}
.offer.bootcamp{left:773px}
.offer.bootcamp .photo{background:linear-gradient(160deg,#efe9dc,#ddd5c6 50%,#b9ad98)}
.offer h3{position:absolute;left:11px;top:86px}
.offer.training h3{font:500 38px/38px "Oswald",sans-serif;color:var(--ink);letter-spacing:-.5px;top:86px}
.offer.group h3{font:700 40px/36px "Arvo",serif;color:var(--ink);left:16px;top:90px}
.offer.bootcamp h3{left:14px;top:62px;width:122px;border:3px solid #3a3a3a;border-left:none;border-right:none;padding:12px 6px;font:700 30px/32px "Arvo",serif;color:#3a3a3a;text-align:center;letter-spacing:1px}
.offer p{position:absolute;left:14px;top:166px;font-size:15.5px;color:var(--ink)}
.offer p strong{font-weight:700}
.offer .btn{position:absolute;left:14px;top:191px;width:72px;height:23px;line-height:23px;font-size:11.5px}
.offer .value{position:absolute;right:12px;top:194px;font-size:15px;color:var(--ink)}
.offer .value strong{font-weight:700}
.video-panel{left:164px;top:754px;width:899px;height:200px}
.video-panel .backdrop{inset:0;background:linear-gradient(90deg,#bcd8ef,#e3eef8 40%,#d6e6f4)}
.video-panel .runners{left:0;top:0;width:260px;height:200px;background:linear-gradient(180deg,#7fb0df,#c9dcec 60%,#8ab1d6)}
.video-panel h2{position:absolute;left:291px;top:26px;font:700 23px "Arvo",serif;color:var(--black)}
.video-panel p{position:absolute;left:291px;top:68px;width:315px;font-size:12px;line-height:17px;color:var(--ink)}
.video-thumb{position:absolute;left:633px;top:20px;width:242px;height:157px;background:linear-gradient(180deg,#6e8a5a,#6f9a3c 45%,#4f7e26);box-shadow:0 3px 6px rgba(0,0,0,.35)}
.video-thumb svg{position:absolute;left:95px;top:50px}
.site-footer{position:absolute;left:162px;right:137px;top:976px;display:flex;justify-content:space-between;font-size:14px;color:var(--white)}
.site-footer nav{display:flex;gap:27px;font-weight:700;font-size:13.5px}
</style>
</head>
<body>
<div class="forest-backdrop" role="img" aria-label="Sunlit green forest with tall tree trunks"></div>

<header class="top-bar">
  <div class="account">MEMBER LOGIN | <span class="signup">SIGN UP</span></div>
  <div class="utility">Time Table | Club Locations</div>
  <div class="social"><span>Linkly</span><span>Chirpr</span></div>
</header>

<div class="brand">Pack<i></i></div>

<div class="call-us"><small>CALL US NOW</small><strong>1300 555 019</strong></div>

<nav class="main-nav">
  <span>HOME</span><span>ABOUT US</span><span>FITNESS</span><span>EVENTS &amp; ADVENTURE</span><span>CONTACT US</span>
</nav>

<section class="panel hero">
  <div class="photo" role="img" aria-label="Two hikers celebrating with arms raised beside a large boulder under a blue sky"></div>
  <h1>No Judgements.<br>No Limits!</h1>
  <ul>
    <li>No Boring Workouts</li>
    <li>No Joining Fees or Long Term Contracts</li>
    <li>Results Guaranteed</li>
  </ul>
  <span class="btn">Check Out Our Plans</span>
  <div class="testimonial">
    <h2>What Our Clients Are Saying</h2>
    <p>“Lorem ipsum dolor sit amet, consectetur ad ipisicing elit, sed do eiusm tempor ine et dolore magna aliqua. sed do eiusm tempor ine et dolore magna aliqua.. <i>Client, Testimonials</i>”</p>
  </div>
</section>

<aside class="panel signup-panel">
  <div class="photo" role="img" aria-label="Wooden background with a climbing carabiner and rope"></div>
  <h2>Get your <em>FREE</em><br><span>Membership Today</span></h2>
  <div class="member-card" role="img" aria-label="Pack membership card"></div>
  <ul class="perks">
    <li>Monthly E-news Hints, Tips &amp; Advice</li>
    <li>VIP invites Events &amp; Adventures</li>
    <li>Special Member Only Offers</li>
    <li>Discounts Card to 20+ Providers</li>
    <li>Valued at $65</li>
  </ul>
  <div class="field name">Name</div>
  <div class="field email">E-mail</div>
  <div class="newsletter"><b>✓</b>Join ur Newsletter</div>
  <span class="btn">Join Now</span>
</aside>

<article class="panel offer training">
  <div class="photo" role="img" aria-label="Couple running through a sunny grassy field"></div>
  <h3>PERSONAL<br>TRAINING</h3>
  <p>Free Initial Consult &amp; Session</p>
  <span class="btn">More Info</span>
  <div class="value">Valued at <strong>$80.00</strong></div>
</article>

<article class="panel offer group">
  <div class="photo" role="img" aria-label="Women stretching arms overhead in an outdoor class"></div>
  <h3>Group<br>Fitness</h3>
  <p>Pass <strong>$25</strong> 7 Days Unlimited Classes</p>
  <span class="btn">More Info</span>
  <div class="value">Valued at <strong>$80.00</strong></div>
</article>

<article class="panel offer bootcamp">
  <div class="photo" role="img" aria-label="Group doing push-ups at an outdoor boot camp"></div>
  <h3>BOOT<br>CAMP</h3>
  <p>Starts Soon Limited Space</p>
  <span class="btn">More Info</span>
  <div class="value">Valued at <strong>$80.00</strong></div>
</article>

<section class="panel video-panel">
  <div class="photo backdrop"></div>
  <div class="photo runners" role="img" aria-label="Man and woman jogging together against a blue sky"></div>
  <h2>Watch Our Demo Video</h2>
  <p>Lorem ipsum dolor sit amet, consectetur adipisicing elit, sed do eiusmod tempor incididunt ut labore et dolore magna aliqua. Ut enim ad minim veniam, quis nostrud exercitation ullamco laboris nisi ut aliquip ex ea commodo consequat. Duis aute irure dolor in reprehenderit in voluptate velit esse cillum dolore eu fugiat nulla pariatur.</p>
  <div class="video-thumb" role="img" aria-label="Outdoor group fitness class stretching on mats in a park">
    <svg width="52" height="52" viewBox="0 0 52 52" aria-hidden="true">
      <circle cx="26" cy="26" r="25" fill="#f39200" stroke="#ffb347" stroke-width="2"/>
      <path d="M20 15 L37 26 L20 37 Z" fill="#ffffff"/>
    </svg>
  </div>
</section>

<footer class="site-footer">
  <span>© 2011 Pack. All Rights Reserved</span>
  <nav><span>Home</span><span>About Us</span><span>Fitness</span><span>Events &amp; Adventure</span><span>Contact Us</span></nav>
</footer>
</body>
</html>
```